Flyer promoting printing services to bars and restaurants

Small print company specialising in print for pubs, bard and restaurants looking for someone to design a flyer promoting our services which will be mailed to a database of potential customers. We have the text but need this putting into a nice design. The text is attached.

Ideally we would want separate versions - one for pubs / bars and another for restaurants.

Target Market(s)

Bars, pubs and restaurants

```html
<!DOCTYPE html>
<html lang="en">
<head>
<meta charset="utf-8">
<title>Marlowe Print – Printing Services for Pubs and Bars</title>
<link rel="stylesheet" href="https://fonts.googleapis.com/css2?family=Lato:wght@400;700&family=Montserrat:wght@300;400;700&family=Oswald:wght@500;700&display=swap">
<style>
  :root{
    --page-bg:#2a2a2a;
    --paper:#ffffff;
    --ink:#222222;
    --grey:#6b6b6b;
    --red:#e51e2b;
    --band-red:#e8333f;
    --deep-red:#a8121c;
    --green:#1e9b48;
    --purple:#7a2f93;
    --orange:#f1901c;
    --magenta:#e0177a;
    --yellow:#f8e51b;
    --blue:#1e9bd7;
    --navy:#2c2f7e;
    --dark-bar:#2b2b2b;
  }
  *{margin:0;padding:0;box-sizing:border-box}
  html,body{width:1200px;height:1200px;overflow:hidden;background:var(--page-bg)}
  .flyer{
    position:absolute;left:245px;top:102px;width:888px;height:1246px;
    background:var(--paper);transform:scale(0.8);transform-origin:0 0;
    font-family:'Lato',sans-serif;color:var(--ink);overflow:hidden;
  }
  .abs{position:absolute}
  .headline{left:50px;top:108px}
  .headline .kicker{font-family:'Montserrat',sans-serif;font-weight:300;font-size:42px;letter-spacing:1px;line-height:1}
  .headline .title{font-family:'Oswald',sans-serif;font-weight:700;font-size:66px;color:var(--red);line-height:1.1;letter-spacing:0.5px}
  .brand{left:560px;top:40px;width:260px;text-align:center}
  .brand .mark{width:44px;height:44px;border-radius:50%;background:var(--red);margin:0 auto 52px}
  .brand .name{font-family:'Oswald',sans-serif;font-weight:500;font-size:34px;letter-spacing:3px;color:var(--ink);line-height:1}
  .brand .tagline{font-family:'Lato',sans-serif;font-weight:400;font-size:18px;color:var(--grey);margin-top:14px}
  .intro{left:43px;top:641px;width:482px;font-size:15px;line-height:19.5px;text-align:justify}
  .promise{left:580px;top:669px;width:270px;text-align:center;font-family:'Montserrat',sans-serif;font-weight:700;font-size:20px;color:var(--deep-red);line-height:26px}
  .services-heading{left:0;top:756px;width:888px;text-align:center;font-family:'Montserrat',sans-serif;font-weight:400;font-size:21px;letter-spacing:0.5px}
  .service-band{left:0;top:790px;width:888px;height:163px;background:var(--band-red)}
  .service-list{position:absolute;list-style:none;color:#fff;font-size:11px;line-height:14px}
  .service-list li{position:relative;margin-bottom:12px}
  .service-list li::before{content:"";position:absolute;left:-22px;top:4px;width:5px;height:5px;border-radius:50%;background:#fff}
  .service-list b{font-weight:700}
  .list-left{left:77px;top:26px;width:310px}
  .list-right{left:501px;top:27px;width:300px}
  .list-right li{margin-bottom:15px}
  .closing{left:37px;top:982px;width:822px;font-size:14.5px;line-height:18px}
  .contact-title{left:0;top:1066px;width:888px;text-align:center;font-family:'Montserrat',sans-serif;font-weight:700;font-size:17px;color:var(--red)}
  .contact-bar{left:234px;top:1098px;width:420px;height:34px;background:var(--dark-bar);color:#fff;font-size:14.5px;text-align:center;line-height:34px}
  .address{left:30px;top:1078px;width:166px;text-align:center;font-size:11px;line-height:14px}
  .web-phone{left:680px;top:1082px;width:136px;text-align:center;font-size:11px;line-height:14px}
  .web-phone svg,.address svg{display:block;margin:0 auto 4px}
  .footer-url{left:606px;top:1212px;font-family:'Montserrat',sans-serif;font-size:14px;letter-spacing:3.5px;color:#fff}
</style>
</head>
<body>
<div class="flyer">
  <svg class="abs" style="left:0;top:0" width="888" height="1246" viewBox="0 0 888 1246" aria-hidden="true">
    <polygon points="0,0 528,0 500,36 0,36" fill="var(--green)"/>
    <rect x="0" y="273" width="86" height="13" fill="var(--purple)"/>
    <rect x="90" y="273" width="92" height="13" fill="var(--orange)"/>
    <rect x="187" y="273" width="92" height="13" fill="var(--magenta)"/>
    <rect x="284" y="273" width="92" height="13" fill="var(--yellow)"/>
    <rect x="381" y="273" width="92" height="13" fill="var(--blue)"/>
    <polygon points="478,273 522,273 512,286 478,286" fill="var(--green)"/>
    <polygon points="526,273 888,258 888,262 536,290 520,296" fill="#b5b5b5"/>
    <rect x="0" y="594" width="78" height="13" fill="var(--purple)"/>
    <rect x="82" y="594" width="92" height="13" fill="var(--orange)"/>
    <rect x="178" y="594" width="92" height="13" fill="var(--magenta)"/>
    <rect x="275" y="594" width="92" height="13" fill="var(--yellow)"/>
    <rect x="372" y="594" width="92" height="13" fill="var(--blue)"/>
    <rect x="468" y="594" width="92" height="13" fill="var(--green)"/>
    <rect x="566" y="594" width="30" height="13" fill="var(--navy)"/>
    <rect x="812" y="594" width="40" height="13" fill="var(--yellow)"/>
    <rect x="856" y="594" width="32" height="13" fill="var(--red)"/>
    <rect x="0" y="1206" width="90" height="13" fill="var(--orange)"/>
    <rect x="94" y="1206" width="92" height="13" fill="var(--magenta)"/>
    <rect x="190" y="1206" width="92" height="13" fill="var(--yellow)"/>
    <rect x="287" y="1206" width="92" height="13" fill="var(--blue)"/>
    <rect x="384" y="1206" width="92" height="13" fill="var(--green)"/>
    <polygon points="481,1206 524,1206 514,1219 481,1219" fill="var(--navy)"/>
    <polygon points="537,1206 888,1206 888,1246 0,1246 0,1230 518,1230" fill="var(--blue)"/>
  </svg>

  <svg class="abs" style="left:0;top:290px" width="888" height="300" role="img" aria-label="Photo of a wide-format printer with print heads laying down a bright yellow and orange print">
    <defs>
      <linearGradient id="printerTone" x1="0" y1="0" x2="1" y2="1">
        <stop offset="0" stop-color="#cfd3d6"/>
        <stop offset="0.45" stop-color="#7d8084"/>
        <stop offset="0.7" stop-color="#f0b21c"/>
        <stop offset="1" stop-color="#e2561b"/>
      </linearGradient>
    </defs>
    <rect x="0" y="0" width="888" height="300" fill="url(#printerTone)"/>
  </svg>

  <svg class="abs" style="left:596px;top:300px" width="220" height="342" role="img" aria-label="Sample printed happy hour drinks flyer for a bar">
    <rect x="0" y="0" width="216" height="340" fill="#2e2e2e"/>
  </svg>

  <div class="abs headline">
    <div class="kicker">Printing Services for</div>
    <div class="title">PUBS AND BARS</div>
  </div>

  <div class="abs brand">
    <div class="mark"></div>
    <div class="name">MARLOWE PRINT</div>
    <div class="tagline">Local print, done properly</div>
  </div>

  <p class="abs intro">Introducing Marlowe Print, an Essex based printing company that prides itself on taking the personalised approach to our customer. We focus on specific sectors to ensure that we meet the requirements of our customers. Pubs and restaurants are one of the sectors in which we have a great deal of experience of providing print for.</p>

  <p class="abs promise">No minimum quantity<br>on any order</p>

  <h2 class="abs services-heading">Some of the printing services we provide</h2>

  <div class="abs service-band">
    <ul class="service-list list-left">
      <li><b>POSTERS &amp; BANNERS:</b> Any size, indoor or outdoor, no minimum quantity, fast turnaround</li>
      <li><b>BRANDED / PERSONALISED CLOTHING:</b> T-shirts, polo-shirts, aprons, chefswear</li>
      <li><b>MENUS:</b> Printed sheets to insert into menu books or free standing folded menus. All formats</li>
    </ul>
    <ul class="service-list list-right">
      <li><b>MULTI-PART NCR ORDER PADS</b> (no carbon required) and note pads</li>
      <li><b>Table talkers / tent cards</b></li>
      <li><b>Flyers and leaflets</b></li>
    </ul>
  </div>

  <p class="abs closing">Whatever your requirements, Marlowe Print offer a fast friendly service using the latest printing technology to produce high quality print. We also have our own in-house design studio and can help out with any design work if required. Please don't hesitate to get in touch and we would be happy to help. We never turn down an excuse to visit the pub!</p>

  <div class="abs contact-title">CONTACT</div>
  <div class="abs contact-bar">Gareth on 01632 960418 or email gareth@marloweprint.uk</div>

  <div class="abs address">
    <svg width="14" height="18" viewBox="0 0 14 18" aria-hidden="true"><path d="M7 1a5.5 5.5 0 0 0-5.5 5.5C1.5 11 7 16.5 7 16.5S12.5 11 12.5 6.5A5.5 5.5 0 0 0 7 1z" fill="none" stroke="#222" stroke-width="1.5"/><circle cx="7" cy="6.5" r="2" fill="#222"/><line x1="3" y1="17" x2="11" y2="17" stroke="#222" stroke-width="1.2"/></svg>
    marlowe print, unit 4 kestrel court, mill lane, brackley, essex, XX1 2YZ
  </div>

  <div class="abs web-phone">
    <svg width="14" height="14" viewBox="0 0 14 14" aria-hidden="true"><circle cx="7" cy="7" r="6" fill="none" stroke="#222" stroke-width="1.3"/><ellipse cx="7" cy="7" rx="2.6" ry="6" fill="none" stroke="#222" stroke-width="1"/><line x1="1" y1="7" x2="13" y2="7" stroke="#222" stroke-width="1"/></svg>
    www.marloweprint.uk
    <svg width="13" height="13" viewBox="0 0 24 24" style="margin-top:2px" aria-hidden="true"><path d="M6.6 10.8a15.1 15.1 0 0 0 6.6 6.6l2.2-2.2a1 1 0 0 1 1-.25 11.4 11.4 0 0 0 3.6.57 1 1 0 0 1 1 1V20a1 1 0 0 1-1 1A17 17 0 0 1 3 4a1 1 0 0 1 1-1h3.5a1 1 0 0 1 1 1c0 1.25.2 2.45.57 3.57a1 1 0 0 1-.25 1z" fill="#222"/></svg>
    01632960418
  </div>

  <div class="abs footer-url">www.marloweprint.uk</div>
</div>
</body>
</html>
```